Stationary Suite for Aussie Law Firm

We are a small law firm operating out of Albany, Western Australia. We have a logo, which we love and was the winner of a ArtHarbor contest last year.
We require a suite of business stationary products incorporating our logo and contact details. These should be:
1. Letterhead (A4)
The letterhead should incorporate the following information in addition to the logo:
ABN 38 902 617 275 (this is our Australian Business Number)
Helena Rusk atf The HTB Family Trust t/as Granite Ridge Law & Settlements (legal name of the business)
Address: Pemberly House, Walcott Street, Albany
Postal Address: PO Box 8170, Albany WA 6332
Telephone: 0491 672 385
Facsimile: 08 9847 2093
Email: info@granitelawgroup.com.au
Website: www.granitelawgroup.com.au
2. Business Card (90mm x 55mm)
I've attached my current business card layout just for your information.
The front of the business card should include the following information in addition to the logo:
Helena Rusk
Director & Principal Solicitor
Telephone: 0491 672 385
Facsimile: 08 9847 2093
Email: helena@granitelawgroup.com.au
The back of the card should be similar to the back of my existing card, but should only have the logo in white and the address of our website (www.granitelawgroup.com.au)
3. Email signature block
This should include the same information as the front of the business card.
4. With Compliments slip (DL size)
The With Compliments slip should include the same information as the Letterhead.
5. Banner (830mm x 2000mm)
We need a banner designed for use at marketing events. This should include our website details and logo - other than that you have fairly free reign with the design.
6. Flyer (DL)
We need a flyer setting out our services and main contact details for use at marketing events. The details to be included are:
Telephone: 0491 672 385
Web: www.granitelawgroup.com.au
Areas of law:
Wills & Estate Planning
Probate & Letters of Administration
Property Law & Conveyancing
General Commercial Law
Business Law
Style guide:
Please look at our website for an idea as to the style of designs we are looking for - www.granitelawgroup.com.au. The design should be modern, sharp and professional.
Colours:
The CMYK details for the colours in our logo are:
Light Blue C72 M5 Y0 K0
Dark Blue C97 M72 Y16 K30
Edit 31/7/2014
I have added a couple of photos that we have used on our website, and additional photos. These are from our local area, so feel free to use these in your designs or to inform them.
- Calibri, Century Gothic

```html
<!DOCTYPE html>
<html lang="en">
<head>
<meta charset="utf-8">
<title>Granite Ridge Law &amp; Settlements – Email Signature</title>
<link rel="stylesheet" href="https://fonts.googleapis.com/css2?family=Carlito:wght@400;700&display=swap">
<style>
  :root {
    --light-blue: #3fb3e6;
    --dark-blue: #1e4c8a;
    --navy-text: #1d3a66;
    --white: #ffffff;
    --page: #ffffff;
  }
  html, body {
    margin: 0;
    padding: 0;
    width: 1200px;
    height: 1200px;
    overflow: hidden;
    background: var(--page);
  }
  .canvas {
    position: relative;
    width: 1200px;
    height: 1200px;
    font-family: "Carlito", "Calibri", sans-serif;
  }
  .signature {
    position: absolute;
    left: 58px;
    top: 420px;
    width: 1084px;
    height: 350px;
  }
  .brand {
    position: absolute;
    left: 4px;
    top: 70px;
    display: flex;
    align-items: center;
    gap: 14px;
    color: var(--dark-blue);
    white-space: nowrap;
  }
  .brand__mark {
    width: 40px;
    height: 40px;
    border-radius: 50%;
    background: var(--light-blue);
    flex: none;
  }
  .brand__name {
    font-size: 32px;
    font-weight: 400;
    line-height: 1;
  }
  .band {
    position: absolute;
    left: 0;
    top: 162px;
    width: 1084px;
    height: 187px;
  }
  .band__shape { position: absolute; inset: 0; }
  .contact { position: absolute; left: 12px; margin: 0; white-space: nowrap; line-height: 1.1; }
  .contact__name { top: 18px; font-size: 22px; color: var(--navy-text); }
  .contact__title { top: 46px; font-size: 17px; color: var(--white); }
  .contact__phones { top: 70px; font-size: 27px; color: var(--white); }
  .contact__phones .label { color: var(--navy-text); }
  .contact__phones .gap { display: inline-block; width: 20px; }
  .contact__email { top: 110px; font-size: 18px; color: var(--navy-text); }
  .contact__email .label { font-size: 15px; }
  .contact__address { top: 140px; font-size: 15px; color: var(--white); line-height: 1.35; }
</style>
</head>
<body>
<main class="canvas">
  <section class="signature" aria-label="Email signature block">
    <div class="brand">
      <span class="brand__mark" aria-hidden="true"></span>
      <span class="brand__name">Granite Ridge Law &amp; Settlements</span>
    </div>

    <div class="band">
      <svg class="band__shape" viewBox="0 0 1084 187" preserveAspectRatio="none" aria-hidden="true">
        <path d="M0,0 L150,0 C320,0 380,99 590,99 L1084,99 L1084,187 L0,187 Z" fill="var(--light-blue)"/>
      </svg>
      <p class="contact contact__name">Helena Rusk</p>
      <p class="contact contact__title">Director &amp; Principal Solicitor</p>
      <p class="contact contact__phones"><span class="label">t:</span> 0491 672 385<span class="gap"></span><span class="label">f:</span> 08 9847 2093</p>
      <p class="contact contact__email"><span class="label">e:</span> helena@granitelawgroup.com.au</p>
      <p class="contact contact__address">Pemberly House, Walcott Street, Albany<br>PO Box 8170, Albany WA 6332</p>
    </div>
  </section>
</main>
</body>
</html>
```